Whitlow Bidhouse on responsive WP

We need a wordpress design for an established auction and real estate company based in Texas. The winning design will incorporate a professional color scheme with company logo in a clean layout. The design needs to consider that this will be developed on a responsive theme. Colors are those that will highlight the logo.

Industry/Entity Type

Real Estate

Font styles to use
Sans Serif

Colors

Designer to choose colors to be used in the design.

Requirements
Must have
• navigation: 1) home 2) Auctions 3) Online Auctions 4) For Sale 5) About Us 6) Our Services 7) Contact Us

design will have slideshow element, either use the attached image or a stock image if it better fits your design

Widgets in the Sidebar: 1) email signup form 2) social media icons - facebook, pinterest, linkedIn, Youtube 3) Featured Auctions widget 4) News& Events blog

footer will have smaller company logo, contact info (below) and attached association logos.

Colors will be that of the logo and white, black/gray and perhaps another highlight color.

Phone: (555) 384-2706
Email: whitlowbidhouse@mailbarn.example
Address: 2715 Marrow Lane, Dellford, TX 70000
Nice to have
• Use of drop menus - for example 1) Upcoming Auctions and 2) Past Auctions under the menu item "Auctions"

```html
<!DOCTYPE html>
<html lang="en">
<head>
<meta charset="utf-8">
<title>Whitlow Bidhouse – Upcoming Auctions</title>
<link href="https://fonts.googleapis.com/css2?family=Open+Sans:wght@400;600;700&family=Arimo:wght@400;700&display=swap" rel="stylesheet">
<style>
  :root{
    --red:#b70000;
    --blue:#0457c8;
    --dark:#3d4545;
    --ink:#222;
    --page:#e2e2e2;
    --panel-line:#dcdcdc;
    --footer:#1f1f1f;
    --field:#e6e6e6;
  }
  *{box-sizing:border-box;margin:0;padding:0}
  html,body{width:900px;height:1200px;overflow:hidden}
  body{background:var(--page);font-family:"Arimo",Arial,sans-serif;color:var(--ink);position:relative}
  .abs{position:absolute}
  .sheet{left:76px;top:0;width:748px;height:1042px;background:#fff}

  .brand{left:92px;top:34px;display:flex;align-items:center;gap:8px}
  .brand-mark{width:18px;height:18px;background:var(--blue)}
  .brand-name{font-family:"Open Sans",sans-serif;font-weight:700;font-size:24px;color:var(--red);letter-spacing:.3px}
  .connect{left:507px;top:56px;font-family:"Open Sans",sans-serif;font-weight:700;font-size:17px;color:#333}
  .social{top:51px;width:30px;height:30px;border-radius:50%}

  .nav{left:76px;top:102px;width:748px;height:38px;background:var(--blue)}
  .nav a{position:absolute;top:0;line-height:38px;color:#fff;text-decoration:none;font-family:"Open Sans",sans-serif;font-weight:700;font-size:10.5px}
  .nav .sep{position:absolute;top:8px;width:1px;height:22px;background:rgba(255,255,255,.35)}
  .dropdown{left:143px;top:147px;width:121px;height:61px;background:var(--blue);border-radius:2px}
  .dropdown .item{height:26px;line-height:26px;padding-left:13px;color:#fff;font-family:"Open Sans",sans-serif;font-size:11px}
  .dropdown .active{background:var(--red);margin-top:6px}
  .drop-arrow{left:163px;top:141px;width:0;height:0;border-left:6px solid transparent;border-right:6px solid transparent;border-bottom:6px solid var(--blue)}

  .hero{left:76px;top:140px;width:540px;height:262px;background:linear-gradient(180deg,#8fb1d9 0%,#cfd6cf 45%,#c7bf9a 62%,#3f8b2c 82%,#58a63a 100%)}
  .signup{left:616px;top:140px;width:208px;height:262px;background:var(--red)}
  .signup-bar{left:616px;top:394px;width:208px;height:8px;background:var(--blue)}
  .signup h2{position:absolute;left:26px;top:16px;font-family:"Open Sans",sans-serif;font-weight:700;font-size:17px;color:#fff}
  .signup p{position:absolute;left:29px;top:39px;font-size:9px;color:#fff;font-family:"Open Sans",sans-serif}
  .field{position:absolute;left:25px;width:165px;height:26px;background:var(--field);border-radius:3px;font-size:10.5px;color:#888;line-height:26px;padding-left:9px;font-family:"Open Sans",sans-serif}
  .subscribe{position:absolute;left:28px;top:214px;width:92px;height:27px;background:#262626;border-radius:4px;color:#fff;font-size:15px;line-height:27px;text-align:center;font-family:"Open Sans",sans-serif}

  .section-title{left:92px;top:422px;font-family:"Open Sans",sans-serif;font-weight:700;font-size:17px;color:var(--red)}

  .card{left:92px;width:468px;height:256px;border:1px solid var(--panel-line);background:#fff}
  .card-head{height:33px;background:var(--blue);color:#fff;font-family:"Open Sans",sans-serif;font-weight:600;font-size:13px;line-height:33px;padding-left:16px;letter-spacing:.2px}
  .box{position:absolute;border:1px solid var(--panel-line);border-radius:3px;background:#fff}
  .thumb{left:14px;top:45px;width:84px;height:68px;padding:4px}
  .thumb .ph{width:100%;height:100%;background:linear-gradient(180deg,#9fc0de,#d8d0bc 55%,#5d8f3c)}
  .links{left:14px;top:125px;width:84px;height:76px}
  .links h3{margin:2px;height:22px;background:var(--red);color:#fff;font-family:"Open Sans",sans-serif;font-size:12px;letter-spacing:.5px;line-height:22px;padding-left:8px;font-weight:600}
  .links .row{display:flex;align-items:center;gap:6px;font-size:10px;font-weight:700;margin:6px 0 0 8px;height:14px}
  .desc{left:106px;top:47px;width:345px;height:81px;padding:6px;font-size:10px;line-height:13.6px;text-transform:uppercase}
  .info{left:106px;top:140px;width:345px;height:105px;padding:6px;font-size:10px;line-height:13.6px}
  .bid-btn{display:block;width:203px;height:24px;margin:5px 0 6px -2px;background:#353535;color:#fff;border-radius:3px;font-weight:700;font-size:10px;line-height:24px;padding-left:9px}
  b{font-weight:700}

  .widget{left:575px;width:236px;border:1px solid var(--panel-line);background:#fff}
  .widget-head{height:34px;background:var(--dark);color:#fff;font-family:"Open Sans",sans-serif;font-size:17px;line-height:36px;padding-left:11px;letter-spacing:.8px}
  .feat-title{position:absolute;left:18px;top:54px;width:205px;font-size:10px;font-weight:700;line-height:13.6px}
  .feat-img{position:absolute;left:8px;top:88px;width:219px;height:89px;background:linear-gradient(180deg,#8fb9e2,#b9cbdc 40%,#8a3a2c 62%,#4f7c33 100%)}
  .feat-date{position:absolute;left:14px;top:192px;width:160px;font-size:10px;line-height:13.6px}
  .feat-foot{position:absolute;left:14px;top:233px;font-size:10px}
  .news{position:absolute;left:8px;display:flex;gap:11px}
  .news .ph{width:53px;height:37px;border:2px solid #ddd;background:linear-gradient(180deg,#d6dce4,#8b3a30 55%,#7a9a62);flex:none}
  .news p{width:152px;font-size:10px;line-height:13.6px}

  .footer{left:0;top:1042px;width:900px;height:126px;background:var(--footer)}
  .footer h4{position:absolute;left:84px;top:24px;color:#ddd;font-family:"Open Sans",sans-serif;font-weight:600;font-size:13px}
  .footer .contact{position:absolute;left:83px;top:61px;color:#fff;font-size:10.5px;line-height:16.4px}
  .badge{position:absolute;background:#d8d8d8}
  .foot-brand{position:absolute;left:664px;top:58px;color:#fff;font-family:"Open Sans",sans-serif;font-weight:700;font-size:16px}
  .copyright{left:0;top:1168px;width:900px;height:32px;background:var(--blue);color:#fff;text-align:center;line-height:32px;font-size:10.5px}
  .copyright u{text-decoration:underline}
</style>
</head>
<body>
  <div class="abs sheet"></div>

  <div class="abs brand"><span class="brand-mark"></span><span class="brand-name">Whitlow Bidhouse</span></div>
  <div class="abs connect">STAY CONNECTED:</div>
  <div class="abs social" style="left:667px;background:var(--blue)" role="img" aria-label="Social network link"></div>
  <div class="abs social" style="left:703px;background:var(--red)" role="img" aria-label="Social network link"></div>
  <div class="abs social" style="left:740px;background:var(--blue)" role="img" aria-label="Social network link"></div>
  <div class="abs social" style="left:779px;background:var(--red)" role="img" aria-label="Video channel link"></div>

  <nav class="abs nav">
    <a style="left:15px">HOME</a><span class="sep" style="left:56px"></span>
    <a style="left:70px">AUCTIONS</a><span class="sep" style="left:135px"></span>
    <a style="left:150px">ONLINE AUCTIONS</a><span class="sep" style="left:256px"></span>
    <a style="left:270px">ABOUT US</a><span class="sep" style="left:336px"></span>
    <a style="left:350px">SERVICES</a><span class="sep" style="left:413px"></span>
    <a style="left:428px">REAL ESTATE LISTINGS</a><span class="sep" style="left:557px"></span>
    <a style="left:573px">REFERENCES</a><span class="sep" style="left:654px"></span>
    <a style="left:669px">CONTACT US</a>
  </nav>

  <div class="abs hero" role="img" aria-label="Slideshow photo of a suburban house with palm tree, lawn and parked SUV"></div>
  <div class="abs drop-arrow"></div>
  <div class="abs dropdown">
    <div class="item active">Upcoming Auctions</div>
    <div class="item">Past Auctions</div>
  </div>

  <aside class="abs signup">
    <h2>EMAIL SIGN UP</h2>
    <p>Sign up for free aution&nbsp; alerts</p>
    <svg style="position:absolute;left:60px;top:60px" width="76" height="72" viewBox="0 0 76 72">
      <rect x="6" y="2" width="68" height="44" rx="4" fill="#fff"/>
      <path d="M6 6 L40 30 L74 6" fill="none" stroke="var(--red)" stroke-width="5"/>
      <path d="M30 68 C30 50 18 44 8 44 L8 52 L-2 40 L8 28 L8 36 C26 36 36 48 30 68Z" fill="#d9d9d9" transform="translate(4 0)"/>
    </svg>
    <div class="field" style="top:135px">Name</div>
    <div class="field" style="top:174px">Email Address</div>
    <div class="subscribe">Subscribe</div>
  </aside>
  <div class="abs signup-bar"></div>

  <h1 class="abs section-title">UPCOMING AUCTIONS</h1>

  <article class="abs card" style="top:457px">
    <div class="card-head">160± ACRES LAND NOBLE COUNTY, OK</div>
    <div class="box thumb"><div class="ph" role="img" aria-label="House with for sale sign"></div></div>
    <div class="box links">
      <h3>LINKS</h3>
      <div class="row"><svg width="16" height="8"><rect width="6" height="7" fill="#111"/><rect x="8" y="0" width="8" height="2" fill="#111"/><rect x="8" y="5" width="8" height="2" fill="#111"/></svg>Details</div>
      <div class="row"><svg width="16" height="14"><rect x="1" y="1" width="10" height="9" fill="none" stroke="#111" stroke-width="1.6"/><rect x="5" y="5" width="10" height="8" fill="#fff" stroke="#111" stroke-width="1.6"/></svg>Photos</div>
    </div>
    <div class="box desc">Billings Area * Crop &amp; Timber<br>160± acres land Noble County, OK ~ Billings area * crop &amp; timber ~ excellent hunting<br>Absolute auction</div>
    <div class="box info">LIVE ON-SITE AUCTION WITH ONLINE BIDDING<br>Begins:&nbsp; Tuesday, March 12, 2013 at 10:00 AM CDT
      <span class="bid-btn">Click here for our online Bidding site</span>
      <b>Location:</b>&nbsp; See Directions<br>United States Billings, OK 74630</div>
  </article>

  <article class="abs card" style="top:744px">
    <div class="card-head">160± ACRES LAND NOBLE COUNTY, OK</div>
    <div class="box thumb"><div class="ph" role="img" aria-label="House with for sale sign"></div></div>
    <div class="box links">
      <h3>LINKS</h3>
      <div class="row"><svg width="16" height="8"><rect width="6" height="7" fill="#111"/><rect x="8" y="0" width="8" height="2" fill="#111"/><rect x="8" y="5" width="8" height="2" fill="#111"/></svg>Details</div>
      <div class="row"><svg width="16" height="14"><rect x="1" y="1" width="10" height="9" fill="none" stroke="#111" stroke-width="1.6"/><rect x="5" y="5" width="10" height="8" fill="#fff" stroke="#111" stroke-width="1.6"/></svg>Photos</div>
    </div>
    <div class="box desc">Billings Area * Crop &amp; Timber<br>160± acres land Noble County, OK ~ Billings area * crop &amp; timber ~ excellent hunting<br>Absolute auction</div>
    <div class="box info">LIVE ON-SITE AUCTION WITH ONLINE BIDDING<br>Begins:&nbsp; Tuesday, March 12, 2013 at 10:00 AM CDT
      <span class="bid-btn">Click here for our online Bidding site</span>
      Location:&nbsp; See Directions<br>United States Billings, OK 74630</div>
  </article>

  <section class="abs widget" style="top:457px;height:257px">
    <div class="widget-head">FEATURED LISTINGS</div>
    <div class="feat-title">Multi Estate &amp; Consignment Auction&nbsp; &amp; Consignment Auction</div>
    <div class="feat-img" role="img" aria-label="Red brick two-storey house under blue sky"></div>
    <div class="feat-date"><b>Start Date/ Time:</b> Saturday, April 13, 2013 At 10:00 Am</div>
    <div class="feat-foot">Multi Estate &amp; Consignment Auction</div>
  </section>

  <section class="abs widget" style="top:744px;height:256px">
    <div class="widget-head">NEWS &amp; EVENTS</div>
    <div class="news" style="top:52px"><div class="ph" role="img" aria-label="Brick house thumbnail"></div><p>Korvane BS3F High Lift, 600 Series Delmar tractor Series Delmar tractor Series Delmar tractor</p></div>
    <div class="news" style="top:119px"><div class="ph" role="img" aria-label="Brick house thumbnail"></div><p>Korvane BS3F High Lift, 600 Series Delmar tractor Series Delmar tractor Series Delmar tractor</p></div>
    <div class="news" style="top:186px"><div class="ph" role="img" aria-label="Brick house thumbnail"></div><p>Korvane BS3F High Lift, 600 Series Delmar tractor Series Delmar tractor Series Delmar tractor</p></div>
  </section>

  <footer class="abs footer">
    <h4>Contact Information</h4>
    <div class="contact">Phone: (555) 384-2706<br>Email: whitlowbidhouse@mailbarn.example<br>Address: 2715 Marrow Lane, Dellford, TX 70000</div>
    <div class="badge" style="left:412px;top:40px;width:42px;height:44px;border-radius:3px" role="img" aria-label="Association badge"></div>
    <div class="badge" style="left:464px;top:38px;width:48px;height:48px;border-radius:50%" role="img" aria-label="Association badge"></div>
    <div class="badge" style="left:522px;top:38px;width:48px;height:48px;border-radius:50%" role="img" aria-label="Association badge"></div>
    <div class="badge" style="left:582px;top:40px;width:58px;height:44px;border-radius:50%" role="img" aria-label="Association badge"></div>
    <div class="foot-brand">Whitlow Bidhouse</div>
  </footer>
  <div class="abs copyright">Copyright © 2014 <u>Whitlow Bidhouse</u>&nbsp; All Rights Reserved.</div>
</body>
</html>
```